Design for a Service-Based Estimate

We want a design for an Estimate that will always be sent in PDF format. The estimate or proposal is a critical document that needs to plainly show the service items, item description but also needs to be attractive and professional looking. Our current estimate deliverable is attached but it looks really basic like a Word document

```html
<!DOCTYPE html>
<html lang="en">
<head>
<meta charset="utf-8">
<title>Firm Slab Estimate</title>
<link rel="stylesheet" href="https://fonts.googleapis.com/css2?family=Open+Sans:wght@400;600;800&display=swap">
<style>
  :root {
    --ink: #33304a;
    --accent: #d9412b;
    --muted: #7a7a7a;
    --line: #8a8a8a;
    --faint: #e3e3e8;
    --paper: #ffffff;
    --band: #3a3452;
  }
  * { margin: 0; padding: 0; box-sizing: border-box; }
  html, body { width: 848px; height: 1200px; overflow: hidden; background: var(--paper); }
  body { font-family: "Open Sans", Arial, sans-serif; color: var(--muted); position: relative; }

  .brand {
    position: absolute; top: 50px; left: 0; width: 848px; text-align: center;
    font-weight: 800; font-size: 52px; letter-spacing: 4px; color: var(--ink); line-height: 1;
  }
  .rule { position: absolute; left: 47px; width: 754px; height: 1px; background: var(--line); }
  .rule--top { top: 148px; }
  .rule--bottom { top: 1146px; }

  .recipient { position: absolute; left: 47px; top: 178px; }
  .recipient__label { font-size: 15px; color: var(--muted); }
  .recipient__name { font-size: 26px; color: var(--ink); margin-top: 2px; line-height: 1.25; }
  .recipient__line { font-size: 15px; line-height: 1.4; }
  .date { position: absolute; right: 47px; top: 201px; font-size: 15px; }

  .project { position: absolute; top: 336px; left: 0; width: 848px; text-align: center; }
  .project__title { font-size: 19px; color: var(--accent); line-height: 1.3; }
  .project__meta { font-size: 15px; line-height: 1.35; }

  .items {
    position: absolute; left: 47px; top: 422px; width: 754px;
    border-collapse: collapse;
  }
  .items th, .items td { border: 1.5px solid var(--line); }
  .items th {
    height: 71px; font-weight: 400; color: var(--accent); font-size: 21px;
    text-align: center; line-height: 1.1;
  }
  .items th.col-item { text-align: left; padding-left: 9px; }
  .items td { font-size: 13.5px; text-align: center; color: var(--muted); }
  .items td.desc { text-align: left; padding: 22px 9px; line-height: 1.45; vertical-align: top; }
  .items tr.row-main td { height: 153px; }
  .items tr.row-option td { height: 68px; }
  .items tr.row-option td.desc { padding-top: 20px; }
  .items td.total { color: var(--accent); font-size: 17px; }
  .col-item { width: 388px; }
  .col-qty { width: 91px; }
  .col-um { width: 91px; }
  .col-unit { width: 91px; }
  .col-total { width: 93px; }

  .grand {
    position: absolute; left: 617px; top: 713px; width: 184px; height: 72px;
    border: 1.5px solid var(--line); border-top: none;
    display: flex; align-items: center; justify-content: center; gap: 8px;
    color: var(--accent); font-size: 17px;
  }

  .brand--faint {
    top: 1052px; font-size: 60px; color: var(--faint);
  }
  .footer-band { position: absolute; left: 0; top: 1163px; width: 848px; height: 37px; background: var(--band); }
</style>
</head>
<body>
  <div class="brand">FIRM SLAB</div>
  <div class="rule rule--top"></div>

  <div class="recipient">
    <div class="recipient__label">To:</div>
    <div class="recipient__name">Dale Whitcombe</div>
    <div class="recipient__line">428 Harbor Lane se Marlow 34902</div>
    <div class="recipient__line">dwhitcombe@mailbox.com</div>
  </div>
  <div class="date">Date:</div>

  <div class="project">
    <div class="project__title">Dale Whitcombe New Concrete Pad</div>
    <div class="project__meta">428 Harbor Lane SE Marlow 34902</div>
    <div class="project__meta">Bid#: 20-0182</div>
  </div>

  <table class="items">
    <thead>
      <tr>
        <th class="col-item">Item</th>
        <th class="col-qty">Quantity</th>
        <th class="col-um">U/M</th>
        <th class="col-unit">Unit<br>$</th>
        <th class="col-total">Total: $</th>
      </tr>
    </thead>
    <tbody>
      <tr class="row-main">
        <td class="desc">Form, Pour &amp; Finish New Concrete Slab (24’ x 24’ x 4”).<br><br>Includes:<br>3000psi Concrete Mix,<br>Footer (12” x 8”) with One Continous Rebar,<br>Wire Mesh Reinforcement and Saw-Cut Expansion Joints</td>
        <td>576</td>
        <td>SF</td>
        <td>$8.65</td>
        <td class="total">$4,982.40</td>
      </tr>
      <tr class="row-option">
        <td class="desc">OPTIONAL: Add (2’ x 24” x 4”) Small Ramp Area</td>
        <td>48</td>
        <td>SF</td>
        <td>$8.65</td>
        <td class="total">$415.20</td>
      </tr>
    </tbody>
  </table>

  <div class="grand"><span>Total Price</span><span>$5,397.60</span></div>

  <div class="brand brand--faint">FIRM SLAB</div>
  <div class="rule rule--bottom"></div>
  <div class="footer-band"></div>
</body>
</html>
```